I would like a minimalist clean and uncluttered website design.
Initially, I would like to see a front page only and would then like to build on the project front there.
RTV logo file with no background is attached, can be grey scale if the designer wishes.
I would like the front page to speak about the company's ethos and goals and I will need to put a great deal of thought into this to ensure it has the desired impact with the content on the subsequent pages.
The paragraph below gives a bit of an idea as to what this will include.
"RTV is a technology company providing approachable IT products and services to business:
With the overwhelming advancements in technology, businesses often find it difficult to determine what is available and what best suits their businesses specific needs.
We can assist business with their IT infrustucture, devices, software in procurement, installation, training, cost control as well as ongoing administration and support. We also keep our Clients informed of new technology and products which can benefit them"
Target Market(s)
Business, Health, Education, Professional Practices. Target age would be around 30 plus either male or female. Office administration level through Managing Directors. English speaking.

```html
<!DOCTYPE html>
<html lang="en">
<head>
<meta charset="utf-8">
<title>RTV – Approachable IT Products and Services</title>
<link rel="stylesheet" href="https://fonts.googleapis.com/css2?family=Josefin+Sans:wght@300;400&family=Open+Sans:wght@300;400&display=swap">
<style>
  :root {
    --dark: #2b2b2b;
    --bar: #303030;
    --ink: #1e1e1e;
    --accent-green: #9bbf45;
    --accent-blue: #3d5088;
    --accent-red: #d81f26;
    --muted: #a8a8a8;
    --rule: #555;
    --white: #ffffff;
    --hero-top: #e6e8ee;
    --hero-mid: #d2d5dc;
    --hero-bottom: #eceef2;
  }
  * { margin: 0; padding: 0; box-sizing: border-box; }
  html, body { width: 1200px; height: 681px; overflow: hidden; }
  body { position: relative; font-family: "Josefin Sans", sans-serif; background: var(--hero-bottom); }

  .hero-visual {
    position: absolute; inset: 0;
    background: linear-gradient(180deg, var(--hero-top) 0%, var(--hero-mid) 55%, var(--hero-bottom) 100%);
  }

  .brand {
    position: absolute; left: 0; top: 0; width: 231px; height: 99px;
    background: var(--dark);
    display: flex; align-items: center; justify-content: center; gap: 12px;
  }
  .brand-mark { width: 22px; height: 22px; background: var(--accent-green); }
  .brand-name { color: var(--white); font-size: 34px; font-weight: 300; letter-spacing: 4px; padding-top: 6px; }

  .social { position: absolute; top: 15px; right: 52px; display: flex; gap: 4px; }
  .social span { width: 21px; height: 21px; border-radius: 50%; background: #9a9a9a; }

  .slide-arrow {
    position: absolute; top: 279px; width: 34px; height: 34px; border-radius: 50%;
    background: rgba(255,255,255,0.3);
  }
  .slide-arrow svg { display: block; }
  .slide-arrow.prev { left: 51px; }
  .slide-arrow.next { left: 1112px; }

  .statement {
    position: absolute; left: 280px; top: 253px; width: 641px; height: 117px;
    border-top: 1px dashed var(--rule); border-bottom: 1px dashed var(--rule);
    font-family: "Open Sans", sans-serif; font-weight: 300; font-size: 26px; line-height: 33px;
    color: var(--ink); text-align: center; padding-top: 20px;
  }
  .statement .more-dots { display: block; line-height: 14px; }

  .learn-more {
    position: absolute; left: 0; width: 1200px; top: 402px; text-align: center;
    font-size: 14px; color: var(--accent-blue); font-weight: 300;
  }
  .cta {
    position: absolute; left: 488px; top: 443px; width: 224px; height: 50px;
    background: var(--accent-red); color: var(--white);
    font-size: 26px; font-weight: 300; letter-spacing: 1px;
    display: flex; align-items: center; justify-content: center; padding-top: 4px;
  }

  .site-footer {
    position: absolute; left: 0; top: 618px; width: 1200px; height: 63px;
    background: var(--bar); display: flex; align-items: center; justify-content: space-between;
    padding: 4px 55px 0 50px;
  }
  .main-nav { display: flex; gap: 31px; }
  .main-nav a { color: var(--white); text-decoration: none; font-size: 15px; font-weight: 300; }
  .main-nav a.current { color: var(--accent-green); }
  .legal { color: var(--muted); font-size: 11px; font-family: "Open Sans", sans-serif; }
</style>
</head>
<body>
  <div class="hero-visual" role="img" aria-label="Soft-focus photo of business people in suits in front of large grey and coloured gears"></div>

  <header class="brand">
    <span class="brand-mark"></span>
    <span class="brand-name">RTV</span>
  </header>

  <div class="social" aria-label="Social links"><span></span><span></span><span></span></div>

  <div class="slide-arrow prev"><svg width="34" height="34" viewBox="0 0 34 34"><path d="M20 11 L14 17 L20 23" fill="none" stroke="#fff" stroke-width="2.5"/></svg></div>
  <div class="slide-arrow next"><svg width="34" height="34" viewBox="0 0 34 34"><path d="M14 11 L20 17 L14 23" fill="none" stroke="#fff" stroke-width="2.5"/></svg></div>

  <section class="statement">
    RTV is a Technology Company Providing<br>
    Approachable IT Products and Services to Business
    <span class="more-dots">...</span>
  </section>

  <p class="learn-more">Learn More</p>
  <a class="cta">Get in Touch</a>

  <footer class="site-footer">
    <nav class="main-nav">
      <a>HOME</a>
      <a class="current">ABOUT US</a>
      <a>PRODUCTS AND SERVICES</a>
      <a>CONTACT US</a>
    </nav>
    <p class="legal">© Copyright 2013 &nbsp;- Terms and Conditions</p>
  </footer>
</body>
</html>
```